I need a design for Corvane Homes which is a custom home builder. The name on it will be Dan Hartley, and I will give the phone number to the winning design. No address or website needed.

```html
<!DOCTYPE html>
<html lang="en">
<head>
<meta charset="UTF-8">
<title>Corvane Homes – Business Card</title>
<link href="https://fonts.googleapis.com/css2?family=Arimo:wght@400&family=Didact+Gothic&display=swap" rel="stylesheet">
<style>
  :root {
    --backdrop: #f3eda6;
    --card-lime: #a2cf0c;
    --brand-green: #0e5b0c;
    --name-green: #1b6d10;
    --phone-ink: #2b2b2b;
    --logo-text: #ffffff;
    --photo-ring: #ffffff;
  }
  * { margin: 0; padding: 0; box-sizing: border-box; }
  html, body {
    width: 1200px;
    height: 1000px;
    overflow: hidden;
    background: var(--backdrop);
  }
  .business-card {
    position: absolute;
    left: 100px;
    top: 215px;
    width: 1000px;
    height: 571px;
    background: var(--card-lime);
    box-shadow: 0 6px 18px rgba(0, 0, 0, 0.18);
  }
  .contact {
    position: absolute;
    left: 62px;
    top: 120px;
  }
  .contact-name {
    font-family: "Didact Gothic", "Century Gothic", sans-serif;
    font-size: 39px;
    font-weight: 400;
    color: var(--name-green);
    letter-spacing: 0.5px;
  }
  .contact-phone {
    margin-top: 2px;
    margin-left: 60px;
    font-family: "Arimo", Arial, sans-serif;
    font-size: 22px;
    color: var(--phone-ink);
    letter-spacing: 0.5px;
  }
  .project-gallery {
    position: absolute;
    left: 52px;
    top: 344px;
    display: flex;
    gap: 16px;
  }
  .project-photo {
    width: 112px;
    height: 112px;
    border-radius: 50%;
    border: 4px solid var(--photo-ring);
    box-shadow: 0 2px 5px rgba(0, 0, 0, 0.25);
  }
  .project-photo.villa { background: linear-gradient(180deg, #9cc6e8 0%, #d8c6a8 55%, #6d9a3e 100%); }
  .project-photo.terrace { background: linear-gradient(180deg, #e9d3ad 0%, #c99a62 60%, #8a6a44 100%); }
  .project-photo.modern { background: linear-gradient(180deg, #c8d2dc 0%, #eef0f1 55%, #7fae4a 100%); }
  .project-photo.cottage { background: linear-gradient(180deg, #8aa6c4 0%, #6b5a4e 55%, #a5b2a8 100%); }
  .brand-badge {
    position: absolute;
    left: 568px;
    top: 93px;
    width: 394px;
    height: 394px;
    border-radius: 50%;
    background: var(--brand-green);
    display: flex;
    flex-direction: column;
    align-items: center;
    justify-content: center;
    padding-top: 150px;
    color: var(--logo-text);
    font-family: "Arimo", Arial, sans-serif;
    font-weight: 400;
  }
  .brand-name {
    font-size: 49px;
    letter-spacing: 0.3px;
  }
  .brand-tagline {
    font-size: 24px;
    margin-top: 2px;
    letter-spacing: 0.5px;
  }
</style>
</head>
<body>
  <section class="business-card">
    <div class="contact">
      <h1 class="contact-name">Dan Hartley</h1>
      <p class="contact-phone">+92 42 5550182</p>
    </div>

    <div class="project-gallery">
      <div class="project-photo villa" role="img" aria-label="Photo of a two-storey villa with garden"></div>
      <div class="project-photo terrace" role="img" aria-label="Photo of a sand-coloured house with balconies"></div>
      <div class="project-photo modern" role="img" aria-label="Photo of a white modern house on a lawn"></div>
      <div class="project-photo cottage" role="img" aria-label="Photo of a gabled family home at dusk"></div>
    </div>

    <div class="brand-badge">
      <p class="brand-name">Corvane Homes</p>
      <p class="brand-tagline">Home Builders</p>
    </div>
  </section>
</body>
</html>
```